Saffron Ember

we need a flyer design. for an A4 sheet folded into 3 layers/pages.
for an Indian fast food take away. Please use up to date UK standard menu design.
Any more info needed can contact us anytime by email.
word document of item for the flyer attached.

Target Market(s)

Indian Food lovers

Industry/Entity Type

Indian Restaurant

Font styles to use
Decorative
Script

Colors
cbe087
abd036
fbf289
f37022

Requirements
Must have
• Can you please bleed the menu so that I can show it to the printer guy
Nice to have
• modern menu

```html
<!DOCTYPE html>
<html lang="en">
<head>
<meta charset="utf-8">
<title>Saffron Ember – Takeaway Menu</title>
<link rel="stylesheet" href="https://fonts.googleapis.com/css2?family=Arvo:wght@400;700&family=Kurale&display=swap">
<style>
  :root{
    --brown:#5b3a2b;
    --brown-dark:#3b2419;
    --green:#8cc63f;
    --green-soft:#a9d36a;
    --red:#e3222a;
    --red-soft:#f08a8d;
    --orange:#f37022;
    --orange-mid:#f7941d;
    --orange-band:#fde1bf;
    --ink:#2b2220;
    --leader:#b9b3ad;
    --panel-top:#ffffff;
    --panel-bottom:#e9e9e9;
  }
  *{box-sizing:border-box;margin:0;padding:0}
  html,body{width:1200px;height:854px;overflow:hidden;background:#fff}
  .menu{position:relative;width:1200px;height:854px;overflow:hidden;font-family:"Kurale",serif;color:var(--ink)}
  .panel{position:absolute;border-radius:14px;background:linear-gradient(160deg,var(--panel-top),var(--panel-bottom));box-shadow:0 1px 3px rgba(0,0,0,.08);z-index:1}
  .shapes{position:absolute;inset:0;z-index:2}
  .heading{position:absolute;z-index:3;color:#fff;font-family:"Kurale",serif;font-size:27px;line-height:1.1;font-weight:400}
  .note{position:absolute;z-index:3;text-align:right;font-size:13px;line-height:16px;color:var(--ink)}
  .list{position:absolute;z-index:3;list-style:none}
  .item{display:flex;align-items:baseline;font-family:"Arvo",serif;font-weight:700;font-size:15.5px;white-space:nowrap}
  .item .num{width:24px;flex:none}
  .item .leader{flex:1;border-bottom:1px dotted var(--leader);margin:0 4px;transform:translateY(-4px)}
  .item .price{font-family:"Kurale",serif;font-weight:400;font-size:15px}
  .sub{font-family:"Kurale",serif;font-size:13px;padding-left:27px;line-height:17px;color:var(--ink)}
  .tag{display:inline-block;width:12px;height:12px;border-radius:50%;color:#fff;font-family:"Arvo",serif;font-size:8.5px;line-height:12px;text-align:center;margin-left:2px;vertical-align:1px}
  .tag:first-of-type{margin-left:6px}

  .kebabs{left:35px;top:146px;width:341px}
  .kebabs li{height:34px}
  .kebabs li.has-sub{height:51.5px}
  .kebabs .item,.bread .item{color:var(--green)}
  .kebabs .item .price,.bread .item .price{color:var(--green)}
  .kebabs .tag,.bread .tag{background:var(--green-soft)}

  .starters{left:37px;top:550px;width:342px}
  .starters li{height:29.8px}
  .starters .item,.biryanis .item{color:var(--red)}
  .starters .tag{background:var(--red-soft)}

  .biryanis{left:825px;top:116px;width:342px}
  .biryanis li{height:29.6px}

  .bread{left:825px;top:521px;width:341px}
  .bread li{height:30px}

  .price-band{position:absolute;left:405px;top:108px;width:387px;height:57px;background:var(--orange-band);z-index:1}
  .price-band dl{position:absolute;display:grid;grid-template-columns:170px 170px;column-gap:7px;row-gap:7px;left:19px;top:10px;font-family:"Arvo",serif;font-weight:700;font-size:14px;color:var(--orange-mid)}
  .price-band .cell{display:flex;align-items:baseline;white-space:nowrap}
  .price-band .cell .leader{flex:1;border-bottom:1px dotted var(--orange-mid);margin:0 3px;transform:translateY(-4px)}
  .price-band .cell .price{font-family:"Kurale",serif;font-weight:400;font-size:15px}
  .price-band .tag{background:#f7b36b}

  .curries{position:absolute;left:422px;top:175px;width:342px;list-style:none;z-index:3}
  .curry{margin-bottom:10.5px}
  .curry .name{display:flex;font-family:"Arvo",serif;font-weight:700;font-size:15.5px;color:var(--orange-mid);line-height:18px}
  .curry .name .num{width:24px;flex:none}
  .curry .name .tag{background:#f7b36b}
  .curry .desc{padding-left:22px;font-size:12.3px;line-height:15.5px;text-align:justify;color:var(--ink)}
</style>
</head>
<body>
<main class="menu">

  <div class="panel" style="left:24px;top:124px;width:362px;height:292px"></div>
  <div class="panel" style="left:24px;top:536px;width:362px;height:282px"></div>
  <div class="panel" style="left:812px;top:102px;width:362px;height:168px"></div>
  <div class="panel" style="left:812px;top:502px;width:362px;height:316px"></div>
  <div class="price-band">
    <dl>
      <div class="cell"><dt>MIX VEG</dt><span class="leader"></span><dd class="price">£5.50</dd></div>
      <div class="cell"><dt>CHICKEN</dt><span class="leader"></span><dd class="price">£6.50</dd></div>
      <div class="cell"><dt>LAMB</dt><span class="leader"></span><dd class="price">£7.50</dd><span class="tag">7</span></div>
      <div class="cell"><dt>PRAWN</dt><span class="leader"></span><dd class="price">£8.50</dd><span class="tag">6</span><span class="tag">4</span></div>
    </dl>
  </div>

  <svg class="shapes" width="1200" height="854" viewBox="0 0 1200 854" aria-hidden="false">
    <defs>
      <linearGradient id="brownFill" x1="0" y1="0" x2="1" y2="1">
        <stop offset="0" stop-color="#6a4433"/>
        <stop offset="1" stop-color="#3b2419"/>
      </linearGradient>
      <linearGradient id="samosaTone" x1="0" y1="0" x2="1" y2="1">
        <stop offset="0" stop-color="#e9d7a8"/>
        <stop offset="0.5" stop-color="#cfa35a"/>
        <stop offset="1" stop-color="#8a9a4a"/>
      </linearGradient>
      <linearGradient id="naanTone" x1="0" y1="0" x2="1" y2="1">
        <stop offset="0" stop-color="#f1efe8"/>
        <stop offset="0.45" stop-color="#f1c94a"/>
        <stop offset="1" stop-color="#e0a83a"/>
      </linearGradient>
      <linearGradient id="curryTone" x1="0" y1="0" x2="1" y2="0">
        <stop offset="0" stop-color="#6b4a35"/>
        <stop offset="0.4" stop-color="#e8632a"/>
        <stop offset="0.7" stop-color="#f2ede6"/>
        <stop offset="1" stop-color="#5a4536"/>
      </linearGradient>
    </defs>

    <!-- kebabs banner -->
    <polygon points="0,0 528,0 0,140" fill="var(--green)"/>
    <polygon points="0,0 512,0 0,118" fill="url(#brownFill)"/>

    <!-- curries banner -->
    <polygon points="432,28 792,104 792,120" fill="var(--orange-mid)"/>
    <polygon points="400,0 792,0 792,104 432,28" fill="url(#brownFill)"/>

    <!-- biryanis banner -->
    <polygon points="792,92 1200,14 792,122" fill="var(--red)"/>
    <polygon points="792,0 1200,0 1200,14 792,92" fill="url(#brownFill)"/>

    <!-- starters -->
    <g role="img" aria-label="Photo of golden vegetable samosas with a fork">
      <polygon points="180,478 404,378 404,553 260,515" fill="url(#samosaTone)"/>
    </g>
    <polygon points="0,536 250,474 0,554" fill="var(--red)"/>
    <polygon points="0,432 250,474 0,536" fill="url(#brownFill)"/>

    <!-- bread & sides -->
    <g role="img" aria-label="Photo of pilau rice and buttery garlic naan">
      <polygon points="824,368 936,276 1200,292 1200,512 1072,448" fill="url(#naanTone)"/>
    </g>
    <polygon points="792,504 1072,400 792,522" fill="var(--green)"/>
    <polygon points="792,364 1072,400 792,504" fill="url(#brownFill)"/>

    <!-- curry photo strip -->
    <g role="img" aria-label="Photo of chicken curry served with basmati rice and spices">
      <rect x="405" y="766" width="387" height="88" fill="url(#curryTone)"/>
    </g>
  </svg>

  <h2 class="heading" style="left:34px;top:34px">Kebabs</h2>
  <h2 class="heading" style="right:424px;top:34px;text-align:right">Curries</h2>
  <h2 class="heading" style="left:812px;top:33px">Biryanis</h2>
  <h2 class="heading" style="left:34px;top:465px">Starters</h2>
  <h2 class="heading" style="left:821px;top:391px">Bread &amp;<br>Side Orders</h2>

  <p class="note" style="right:818px;top:69px">All kebabs served<br>with fresh Naan bread,<br>mixed salad, chilli garlic sauce</p>
  <p class="note" style="right:29px;top:65px">All biryanis served<br>with curry sauce</p>

  <ul class="list kebabs">
    <li><div class="item"><span class="num">1.</span>Doner Kebab<span class="tag">7</span><span class="tag">8</span><span class="leader"></span><span class="price">£ 6.00</span></div></li>
    <li><div class="item"><span class="num">2.</span>Chicken Tikka Kebab<span class="tag">7</span><span class="tag">8</span><span class="leader"></span><span class="price">£ 5.00</span></div></li>
    <li class="has-sub"><div class="item"><span class="num">3.</span>Mixed Kebab<span class="tag">7</span><span class="tag">8</span><span class="leader"></span><span class="price">£ 6.00</span></div><p class="sub">(Chicken &amp; Doner)</p></li>
    <li class="has-sub"><div class="item"><span class="num">4.</span>Doner Kebab Box<span class="leader"></span><span class="price">£6.00</span></div><p class="sub">(With chips, salad &amp; sauce)</p></li>
    <li class="has-sub"><div class="item"><span class="num">5.</span>Mixed Kebab Box<span class="leader"></span><span class="price">£7.00</span></div><p class="sub">(With chips, salad &amp; sauce)</p></li>
    <li class="has-sub"><div class="item"><span class="num">6.</span>Southern Fried Chicken Box<span class="leader"></span><span class="price">£5.00</span></div><p class="sub">(With chips)</p></li>
  </ul>

  <ul class="list starters">
    <li><div class="item"><span class="num">1.</span>Chicken Nuggets<span class="leader"></span><span class="price">£ 3.00</span></div></li>
    <li><div class="item"><span class="num">2.</span>Spicy Chicken Wings<span class="leader"></span><span class="price">£ 3.50</span></div></li>
    <li><div class="item"><span class="num">3.</span>Veg Samosa<span class="tag">8</span><span class="leader"></span><span class="price">£ 3.50</span></div></li>
    <li><div class="item"><span class="num">4.</span>Spring Roll<span class="leader"></span><span class="price">£ 4.00</span></div></li>
    <li><div class="item"><span class="num">5.</span>Onion Bhaji<span class="leader"></span><span class="price">£ 3.50</span></div></li>
    <li><div class="item"><span class="num">6.</span>Chicken Tikka<span class="tag">7</span><span class="leader"></span><span class="price">£ 3.50</span></div></li>
    <li><div class="item"><span class="num">7.</span>Veg Pakora<span class="leader"></span><span class="price">£ 3.00</span></div></li>
    <li><div class="item"><span class="num">8.</span>Onion Rings<span class="leader"></span><span class="price">£ 2.00</span></div></li>
    <li><div class="item"><span class="num">9.</span>Chicken Pakora<span class="leader"></span><span class="price">£ 3.00</span></div></li>
  </ul>

  <ol class="curries">
    <li class="curry"><div class="name"><span class="num">1.</span>Saffron Ember special curry<span class="tag">2</span><span class="tag">7</span></div><p class="desc">Traditional Indian chicken curry to suit most plates mild, medium or hot – you choose!</p></li>
    <li class="curry"><div class="name"><span class="num">2.</span>Tikka Masala<span class="tag">7</span></div><p class="desc">Cooked in a smooth creamy tomato sauce</p></li>
    <li class="curry"><div class="name"><span class="num">3.</span>Royal Korma<span class="tag">2</span><span class="tag">7</span></div><p class="desc">Cooked in a rich, creamy sauce with coconut</p></li>
    <li class="curry"><div class="name"><span class="num">4.</span>South Indian Garlic Chilli</div><p class="desc">Tasty red curry loaded with garlic, ground spices and green chilli</p></li>
    <li class="curry"><div class="name"><span class="num">5.</span>Saag<span class="tag">7</span></div><p class="desc">Cooked with spinach, fresh herbs, plum tomato sauce</p></li>
    <li class="curry"><div class="name"><span class="num">6.</span>Madras</div><p class="desc">Hot spicy red tomato based curry sauce</p></li>
    <li class="curry"><div class="name"><span class="num">7.</span>Do-Piazza</div><p class="desc">Cooked with fresh tomato sauce and loaded with onions</p></li>
    <li class="curry"><div class="name"><span class="num">8.</span>Bhuna</div><p class="desc">Cooked in rich sauce with fresh onion, tomato, garlic and ginger</p></li>
    <li class="curry"><div class="name"><span class="num">9.</span>Jalfarji<span class="tag">2</span><span class="tag">7</span></div><p class="desc">Strips of onion, pepper cooked in creamy almond sauce</p></li>
    <li class="curry"><div class="name"><span class="num">10.</span>Roganjosh</div><p class="desc">A red curry delicacy from Kashmir</p></li>
    <li class="curry"><div class="name"><span class="num">11.</span>Karahi</div><p class="desc">Cooked with onions, peppers and chefs special spicy sauce</p></li>
  </ol>

  <ul class="list biryanis">
    <li><div class="item"><span class="num">1.</span>Chicken Biryani<span class="leader"></span><span class="price">£ 7.50</span></div></li>
    <li><div class="item"><span class="num">2.</span>Lamb Biryani<span class="leader"></span><span class="price">£ 8.00</span></div></li>
    <li><div class="item"><span class="num">3.</span>Prawn Biryani<span class="leader"></span><span class="price">£ 8.00</span></div></li>
    <li><div class="item"><span class="num">4.</span>Vegetable Biryani<span class="leader"></span><span class="price">£ 7.00</span></div></li>
    <li><div class="item"><span class="num">5.</span>Mix Biryani<span class="leader"></span><span class="price">£ 8.50</span></div></li>
  </ul>

  <ul class="list bread">
    <li><div class="item"><span class="num">1.</span>Plain Naan<span class="tag">7</span><span class="tag">8</span><span class="leader"></span><span class="price">£ 1.80</span></div></li>
    <li><div class="item"><span class="num">2.</span>Garlic Naan<span class="tag">7</span><span class="tag">8</span><span class="leader"></span><span class="price">£ 2.00</span></div></li>
    <li><div class="item"><span class="num">3.</span>Keema Naan<span class="tag">7</span><span class="tag">8</span><span class="leader"></span><span class="price">£ 2.50</span></div></li>
    <li><div class="item"><span class="num">4.</span>Peshwari Naan<span class="tag">2</span><span class="tag">7</span><span class="tag">8</span><span class="leader"></span><span class="price">£ 2.50</span></div></li>
    <li><div class="item"><span class="num">5.</span>Cheese Naan<span class="tag">7</span><span class="tag">8</span><span class="leader"></span><span class="price">£ 2.50</span></div></li>
    <li><div class="item"><span class="num">6.</span>Garlic Chilli Naan<span class="tag">7</span><span class="tag">8</span><span class="leader"></span><span class="price">£ 3.00</span></div></li>
    <li><div class="item"><span class="num">7.</span>Poppadum with dip<span class="leader"></span><span class="price">£ 1.50</span></div></li>
    <li><div class="item"><span class="num">8.</span>Pilau Rice<span class="leader"></span><span class="price">£ 1.80</span></div></li>
    <li><div class="item"><span class="num">9.</span>Boiled Basmati<span class="leader"></span><span class="price">£ 1.60</span></div></li>
    <li><div class="item"><span class="num">10.</span>Curry Chips<span class="leader"></span><span class="price">£ 3.00</span></div></li>
  </ul>

</main>
</body>
</html>
```